Kestrel Roofing & Restoration Business Card Design

Lookiing for a double sided business card design that will have rounded corners, will look good with Spot UV, Soft Laminate, or Gloss
Front of card should have Logo, Name and Contact Info, License numbers
Back of card should have Logo, maybe other small details

```html
<!DOCTYPE html>
<html lang="en">
<head>
<meta charset="utf-8">
<title>Kestrel Roofing &amp; Restoration – Business Card</title>
<link rel="stylesheet" href="https://fonts.googleapis.com/css2?family=Montserrat:wght@400;500;700&family=Poppins:wght@600&display=swap">
<style>
  :root {
    --backdrop: #bcbdbf;
    --sky: #1baae2;
    --ink: #06090b;
    --paper: #ffffff;
    --text: #222326;
  }
  * { margin: 0; padding: 0; box-sizing: border-box; }
  html, body { width: 1200px; height: 1200px; overflow: hidden; background: var(--backdrop); }
  .sheet { position: relative; width: 1200px; height: 1200px; }

  .card {
    position: absolute; left: 308px; width: 583px; height: 339px;
    background: var(--paper); overflow: hidden;
  }
  .card--front { top: 222px; }
  .card--back { top: 638px; }
  .card-shapes { position: absolute; inset: 0; width: 100%; height: 100%; }

  .wordmark {
    position: absolute; color: var(--paper);
    font-family: "Poppins", sans-serif; font-weight: 600;
    text-align: center; line-height: 1.15; letter-spacing: 0.2px;
  }
  .card--front .wordmark { left: 49px; width: 207px; top: 144px; font-size: 14px; }
  .card--back .wordmark { left: 0; width: 583px; top: 143px; font-size: 24px; }

  .company-title {
    position: absolute; left: 322px; top: 66px;
    font-family: "Montserrat", sans-serif; font-weight: 700;
    font-size: 21px; line-height: 28px; color: var(--ink); letter-spacing: 0.1px;
  }
  .title-rule { position: absolute; left: 322px; top: 125px; width: 62px; height: 3px; background: var(--sky); }

  .contact-list { list-style: none; }
  .contact-item {
    position: absolute; left: 321px; display: flex; align-items: flex-start; gap: 10px;
    font-family: "Montserrat", sans-serif; font-weight: 400; font-size: 11px;
    line-height: 13.5px; color: var(--text);
  }
  .contact-item svg { flex: none; width: 21px; height: 21px; }
  .contact-item span { padding-top: 3px; }
  .contact-item--address { top: 166px; }
  .contact-item--phone { top: 221px; }
  .contact-item--email { top: 248px; }
  .contact-item--web { top: 276px; }
</style>
</head>
<body>
<main class="sheet">

  <section class="card card--front" aria-label="Card front">
    <svg class="card-shapes" viewBox="0 0 583 339" aria-hidden="true">
      <rect x="0" y="0" width="177" height="339" fill="var(--sky)"/>
      <rect x="129" y="0" width="48" height="339" fill="var(--ink)"/>
      <polygon points="129,65 177,65 256,108 256,232 177,274 129,274 49.5,232 49.5,108" fill="var(--ink)"/>
    </svg>
    <div class="wordmark">KESTREL ROOFING<br>&amp; RESTORATION</div>

    <h1 class="company-title">KESTREL ROOFING<br>&amp; RESTORATION</h1>
    <div class="title-rule"></div>

    <ul class="contact-list">
      <li class="contact-item contact-item--address">
        <svg viewBox="0 0 22 22" aria-hidden="true"><circle cx="11" cy="11" r="11" fill="var(--sky)"/><path d="M11 5.5a3.6 3.6 0 0 0-3.6 3.6c0 2.7 3.6 6.9 3.6 6.9s3.6-4.2 3.6-6.9A3.6 3.6 0 0 0 11 5.5z" fill="#fff"/><circle cx="11" cy="9.1" r="1.3" fill="var(--sky)"/></svg>
        <span>alder road, Northfield,<br>United Kingdom</span>
      </li>
      <li class="contact-item contact-item--phone">
        <svg viewBox="0 0 22 22" aria-hidden="true"><circle cx="11" cy="11" r="11" fill="var(--sky)"/><path d="M8.2 6.2l1.3-.3 1.1 2.5-1 .9a6.5 6.5 0 0 0 3.1 3.1l.9-1 2.5 1.1-.3 1.3c-.2.7-.9 1.1-1.6 1A8.6 8.6 0 0 1 7.2 7.8c-.1-.7.3-1.4 1-1.6z" fill="#fff"/></svg>
        <span>+44 7700 900318</span>
      </li>
      <li class="contact-item contact-item--email">
        <svg viewBox="0 0 22 22" aria-hidden="true"><circle cx="11" cy="11" r="11" fill="var(--sky)"/><rect x="6" y="7.5" width="10" height="7" rx="1" fill="#fff"/><path d="M6.5 8l4.5 3.5L15.5 8" fill="none" stroke="var(--sky)" stroke-width="1"/></svg>
        <span>hello@kestrelroof.co.uk</span>
      </li>
      <li class="contact-item contact-item--web">
        <svg viewBox="0 0 22 22" aria-hidden="true"><circle cx="11" cy="11" r="11" fill="var(--sky)"/><g fill="none" stroke="#fff" stroke-width="1.1"><circle cx="11" cy="11" r="5"/><ellipse cx="11" cy="11" rx="2.2" ry="5"/><path d="M6 11h10"/></g></svg>
        <span>http://www.kestrelroof.co.uk</span>
      </li>
    </ul>
  </section>

  <section class="card card--back" aria-label="Card back">
    <svg class="card-shapes" viewBox="0 0 583 339" aria-hidden="true">
      <rect x="0" y="0" width="583" height="339" fill="var(--sky)"/>
      <polygon points="79.5,0 400.5,0 583,159 583,262 505,339 182,339 0,182 0,79" fill="var(--ink)"/>
    </svg>
    <div class="wordmark">KESTREL ROOFING<br>&amp; RESTORATION</div>
  </section>

</main>
</body>
</html>
```